Design a "healthy, happy dog and cat" cheque/check background

I am looking for a few design concepts featuring a happy healthy dog and cat, that will be used as the background of a paper cheque/check.

This will require Photoshop and stock photos.

Here is the design brief: https://files.brivontel.net/sheet/48kQmZ2xTrWvLpN7aHcYeJ5uBdFsKo9GiRtXnVw3Lz/view?share=on

Colors

Designer to choose colors to be used in the design.

Requirements
Must have
• A happy dog and cat the main focus within the "empty" central part of the cheque/check, and a complementary background for the rest of the cheque, following the design guidelines in the attached google doc.

```html
<!DOCTYPE html>
<html lang="en">
<head>
<meta charset="utf-8">
<title>Pet Cheque</title>
<link href="https://fonts.googleapis.com/css2?family=Arimo:wght@400;700&family=Share+Tech+Mono&display=swap" rel="stylesheet">
<style>
  :root {
    --page: #ffffff;
    --peach: #f9dac8;
    --pink: #eec9d9;
    --lavender: #e0b6e6;
    --ink: #1c1c1c;
    --rule: #3a3a3a;
    --field: #ffffff;
    --pet-light: #eeeeee;
    --pet-mid: #b9b9bd;
    --pet-dark: #8a8a90;
  }
  * { margin: 0; padding: 0; box-sizing: border-box; }
  html, body {
    width: 1200px; height: 544px; overflow: hidden;
    background: var(--page);
    font-family: "Arimo", Arial, sans-serif;
    color: var(--ink);
  }
  .canvas { position: relative; width: 1200px; height: 544px; }
  .cheque {
    position: absolute; left: 24px; top: 20px; width: 1168px; height: 388px;
    background: linear-gradient(90deg, var(--peach) 0%, var(--pink) 45%, var(--lavender) 100%);
  }
  .abs { position: absolute; white-space: nowrap; }
  .account-holder { left: 34px; top: 40px; line-height: 1.15; }
  .account-holder .name { font-size: 21px; font-weight: 700; letter-spacing: 0.3px; color: #333; }
  .account-holder .line { font-size: 18px; color: #333; }
  .cheque-number { left: 1000px; top: 28px; font-size: 23px; font-weight: 700; }
  .date-label { left: 760px; top: 99px; font-size: 19px; }
  .date-boxes { left: 824px; top: 70px; display: flex; gap: 2.3px; }
  .date-box { width: 37px; height: 37px; background: var(--field); }
  .date-keys { left: 824px; top: 112px; display: flex; gap: 2.3px; }
  .date-keys span { width: 37px; text-align: center; font-size: 13px; }
  .payee-label { left: 32px; top: 170px; font-size: 13px; line-height: 0.95; }
  .pet-photo {
    left: 372px; top: 20px; width: 440px; height: 338px;
    border-radius: 46% 46% 12px 12px / 30% 30% 12px 12px;
    background: radial-gradient(ellipse at 62% 40%, var(--pet-light) 0%, #d7d7da 45%, var(--pet-mid) 75%, transparent 100%);
  }
  .rules { left: 0; top: 0; width: 1168px; height: 388px; }
  .dollar { left: 930px; top: 168px; font-size: 31px; }
  .amount-box { left: 948px; top: 154px; width: 194px; height: 48px; background: var(--field); }
  .amount-words { left: 894px; top: 233px; font-size: 14px; }
  .bank { left: 32px; top: 272px; display: flex; align-items: flex-start; gap: 12px; }
  .bank-dot { width: 52px; height: 52px; border-radius: 50%; background: var(--ink); margin-top: 6px; }
  .bank-text { line-height: 1.12; }
  .bank-text .name { font-size: 19px; font-weight: 700; }
  .bank-text .line { font-size: 18px; }
  .company-name { left: 786px; top: 313px; font-size: 14px; }
  .memo { left: 37px; top: 364px; font-size: 11px; }
  .security-badge {
    left: 1136px; top: 252px; width: 30px; height: 134px;
    border: 1.5px solid #555; border-radius: 3px;
  }
  .micr {
    position: absolute; left: 52px; top: 448px;
    font-family: "Share Tech Mono", "Courier New", monospace;
    font-size: 27px; letter-spacing: 2px; color: #111; white-space: nowrap;
  }
</style>
</head>
<body>
<div class="canvas">
  <section class="cheque">
    <div class="abs pet-photo" role="img" aria-label="Photo of a happy grey cat lying beside a smiling white and grey husky dog"></div>

    <svg class="abs rules" viewBox="0 0 1168 388" aria-hidden="true">
      <line x1="32" y1="202" x2="898" y2="202" stroke="#3a3a3a" stroke-width="1.2"/>
      <line x1="898" y1="170" x2="898" y2="202" stroke="#3a3a3a" stroke-width="1.2"/>
      <line x1="32" y1="256" x2="880" y2="256" stroke="#3a3a3a" stroke-width="1.2"/>
      <line x1="880" y1="256" x2="888" y2="220" stroke="#3a3a3a" stroke-width="1.2"/>
      <line x1="32" y1="378" x2="560" y2="378" stroke="#3a3a3a" stroke-width="1.2"/>
      <line x1="662" y1="378" x2="1074" y2="378" stroke="#3a3a3a" stroke-width="1.2"/>
    </svg>

    <div class="abs account-holder">
      <div class="name">Maplecrest Cheques Personal Cheque</div>
      <div class="line">48 Larkspur Lane</div>
      <div class="line">Brookhaven, Ontario K0K 2B0</div>
    </div>

    <div class="abs cheque-number">101</div>

    <div class="abs date-label">DATE</div>
    <div class="abs date-boxes">
      <div class="date-box"></div><div class="date-box"></div><div class="date-box"></div><div class="date-box"></div>
      <div class="date-box"></div><div class="date-box"></div><div class="date-box"></div><div class="date-box"></div>
    </div>
    <div class="abs date-keys">
      <span>D</span><span>D</span><span>M</span><span>M</span><span>Y</span><span>Y</span><span>Y</span><span>Y</span>
    </div>

    <div class="abs payee-label">PAY TO THE<br>ORDER OF</div>
    <div class="abs dollar">$</div>
    <div class="abs amount-box"></div>
    <div class="abs amount-words">100 DOLLARS</div>

    <div class="abs bank">
      <div class="bank-dot" aria-hidden="true"></div>
      <div class="bank-text">
        <div class="name">Your Financial Institution</div>
        <div class="line">200 Finance Avenue</div>
        <div class="line">Your City, Your Province A1B 2CS</div>
      </div>
    </div>

    <div class="abs company-name">Optional Company Name</div>
    <div class="abs memo">MEMO</div>
    <div class="abs security-badge" aria-hidden="true"></div>
  </section>

  <div class="micr">⑈101⑈ ⑆12345⑉678⑆ 12345⑉6789⑈</div>
</div>
</body>
</html>
```